Southern Rigline Academy needs a modern website that oozes professionalism

Our current website is boring and looks like everyone elses. We need a modern website that says we are the best at plant operator training. We use Varnhold and Delvaro equipment for our training. We train all over Australia in Civil Construction, Mining and Quarrying. We want to be the "Go to" website for all plant operator training in Australia.

Industry/Entity Type

Heavy Machinery Training

Colors
0054AA
0677BA
7BADD7
CADEEF
E8F1F8
FFF300
FFF600
FEFA6F
FFFEC7
FFFEE8

```html
<!DOCTYPE html>
<html lang="en">
<head>
<meta charset="utf-8">
<title>Southern Rigline Academy — Plant Operator Training</title>
<link href="https://fonts.googleapis.com/css2?family=Ubuntu:wght@400;500;700&family=Lato:wght@400;700;900&display=swap" rel="stylesheet">
<style>
:root{
  --navy:#17315f;
  --navy-deep:#0f1a33;
  --navy-bar:#1c2742;
  --blue:#0054aa;
  --blue-text:#3b5b9c;
  --sky:#7badd7;
  --ice:#e8f1f8;
  --yellow:#ffc20e;
  --yellow-soft:#fffec7;
  --ink:#1b2238;
  --grey:#5d6270;
  --light:#f5f6f8;
  --white:#ffffff;
}
*{box-sizing:border-box;margin:0;padding:0}
html,body{width:1200px;height:5220px;overflow:hidden}
body{position:relative;font-family:"Lato",sans-serif;color:var(--ink);background:var(--white)}
.abs{position:absolute}
.heading{font-family:"Ubuntu",sans-serif;font-weight:500;color:var(--navy)}
.eyebrow{font-family:"Lato",sans-serif;font-weight:900;font-size:10px;letter-spacing:.5px;color:var(--yellow);text-transform:uppercase}
.photo{position:absolute}
.btn{position:absolute;display:flex;align-items:center;justify-content:center;font-weight:900;font-size:14px}

/* header */
.site-header{position:absolute;left:0;top:0;width:1200px;height:126px;background:var(--white);z-index:3}
.top-contact{position:absolute;top:22px;display:flex;align-items:center;gap:12px;font-size:10px;color:var(--grey)}
.top-contact .dot{width:30px;height:30px;border-radius:50%;background:var(--navy);display:flex;align-items:center;justify-content:center}
.top-contact b{display:block;color:var(--ink);font-size:11px}
.appointment{left:880px;top:14px;width:182px;height:39px;border-radius:20px;background:var(--navy);color:var(--white);font-size:11px;font-weight:700}
.header-rule{position:absolute;top:70px;left:120px;width:940px;height:1px;background:#e4e6ea}
.nav a{position:absolute;top:90px;font-size:11px;color:var(--grey);text-decoration:none}
.logo-tab{position:absolute;left:499px;top:40px;width:190px;height:108px;background:var(--white);border-radius:0 0 22px 22px;z-index:2;display:flex;align-items:center;justify-content:center;gap:8px}
.brand{font-family:"Ubuntu",sans-serif;font-weight:700;color:var(--navy);font-size:15px;line-height:1.05;text-transform:uppercase}
.brand-mark{width:26px;height:26px;border-radius:50%;background:var(--yellow);flex:none}

/* hero */
.hero-photo{left:0;top:126px;width:1200px;height:758px;background:linear-gradient(120deg,#3b3a35 0%,#55524a 40%,#6b6452 65%,#3e3b33 100%)}
.hero-photo::after{content:"";position:absolute;inset:0;background:rgba(20,20,20,.35)}
.hero-kicker{left:106px;top:366px;color:var(--white);font-family:"Ubuntu",sans-serif;font-size:20px;font-weight:500;letter-spacing:6px}
.hero-title{left:100px;top:398px;color:var(--white);font-family:"Ubuntu",sans-serif;font-size:60px;font-weight:500;letter-spacing:1px}
.hero-line{left:101px;top:485px;width:629px;height:2px;background:var(--yellow)}
.hero-copy{left:106px;top:506px;width:640px;color:var(--white);font-size:16px;line-height:28px}
.learn{left:107px;top:594px;width:144px;height:38px;border-radius:20px;background:var(--yellow);color:var(--white);font-size:13px}
.quote{left:264px;top:594px;width:178px;height:38px;border-radius:20px;background:#0b0b0b;color:var(--white);font-size:13px}

/* features */
.feature{position:absolute;top:807px;width:318px;height:281px;background:var(--white);border-radius:6px;box-shadow:0 4px 18px rgba(0,0,0,.1);text-align:center}
.feature .icon{width:64px;height:64px;border-radius:50%;background:var(--ice);margin:30px auto 0;display:flex;align-items:center;justify-content:center}
.feature h3{font-family:"Ubuntu",sans-serif;font-weight:500;color:var(--navy);font-size:18px;margin-top:38px}
.feature p{color:var(--blue-text);font-size:13px;line-height:26px;margin:12px auto 0;width:250px}

/* about */
.about-title{left:95px;top:1198px;font-size:34px;line-height:53px}
.about-copy{left:95px;top:1316px;width:420px;font-size:13px;line-height:25.2px;color:var(--grey)}
.contact-btn{left:97px;top:1547px;width:154px;height:44px;background:var(--yellow);color:var(--white);gap:14px}
.about-photo{left:602px;top:1186px;width:498px;height:405px;border-radius:6px;background:linear-gradient(160deg,#b9c4c9 0%,#a08a5e 45%,#e07a2c 70%,#6d5a3e 100%)}
.badge{left:586px;top:1353px;width:40px;height:40px;border-radius:50%;background:var(--white);box-shadow:0 2px 8px rgba(0,0,0,.2);display:flex;align-items:center;justify-content:center}

/* services */
.services{left:0;top:1688px;width:1200px;height:632px;background:var(--light)}
.center{width:1200px;text-align:center;left:0}
.section-copy{font-size:13px;line-height:24px;color:var(--grey)}
.service{position:absolute;top:1928px;width:320px;height:285px;border-radius:6px}
.service-label{position:absolute;top:2185px;width:245px;height:51px;background:var(--white);border-radius:4px;box-shadow:0 3px 10px rgba(0,0,0,.1);display:flex;align-items:center;justify-content:center;font-family:"Ubuntu",sans-serif;font-weight:500;color:var(--navy);font-size:20px}

/* call band */
.call-band{left:0;top:2320px;width:1200px;height:309px;background:linear-gradient(90deg,#1d1c1a 0%,#2f2d2a 50%,#1f1e1c 100%)}
.call-text{top:2434px;color:var(--white);font-family:"Ubuntu",sans-serif;font-size:33px;line-height:40px}
.call-text span{color:var(--yellow)}
.call-pill{left:351px;top:2596px;width:500px;height:57px;background:var(--white);border-radius:4px;box-shadow:0 3px 12px rgba(0,0,0,.15);display:flex;align-items:center;justify-content:space-around;font-size:16px;padding:0 20px}

/* projects */
.projects-bg{left:0;top:2629px;width:1200px;height:669px;background:var(--light)}
.project{position:absolute;top:2826px;width:284px;height:316px}
.project-label{position:absolute;top:3085px;width:168px;height:57px;background:var(--white);padding:16px 0 0 16px;font-weight:900;font-size:13px;line-height:15px;color:var(--ink)}
.projects-btn{left:553px;top:3195px;width:154px;height:48px;background:var(--yellow);color:var(--white);gap:14px}

/* why */
.why-photo{left:0;top:3298px;width:1200px;height:604px;background:linear-gradient(100deg,#5d7890 0%,#9a8a74 35%,#d79a52 55%,#e0c23c 75%,#4a4237 100%)}
.why-card{left:93px;top:3367px;width:491px;height:464px;background:var(--white);border-radius:8px}
.why-item{position:absolute;left:50px;width:400px;display:flex;gap:22px}
.why-item .ic{width:40px;flex:none;padding-top:4px}
.why-item h4{color:var(--blue);font-size:12px;font-weight:900;margin-bottom:6px}
.why-item p{font-size:12px;line-height:25px;color:var(--grey)}

/* contact */
.form-card{left:140px;top:4119px;width:910px;height:474px;background:var(--white);border-radius:8px;box-shadow:0 4px 24px rgba(0,0,0,.08)}
.field{position:absolute;border:1.5px solid var(--blue);border-radius:20px;font-size:12px;color:var(--grey);font-style:italic;padding:18px 0 0 36px}
.field.active{background:#e3f0f8;border-color:var(--sky);color:var(--sky)}
.field label{position:absolute;top:-9px;left:30px;background:var(--white);padding:0 6px;font-style:normal;color:var(--ink);font-size:12px}
.field.active label{background:transparent;color:var(--blue)}
.social{position:absolute;top:4515px;width:28px;height:28px;border-radius:50%;border:1.5px solid var(--blue)}
.submit{left:843px;top:4510px;width:144px;height:39px;border-radius:20px;background:var(--yellow);color:var(--white);font-size:12px;gap:12px}
.submit i{width:22px;height:22px;border-radius:50%;background:var(--white);display:inline-block}

/* footer */
.footer{left:0;top:4697px;width:1200px;height:464px;background:var(--navy-deep)}
.foot-social{position:absolute;top:4761px;width:38px;height:38px;border-radius:3px;background:#2d5fa8}
.footer-brand{left:410px;top:4742px;width:380px;height:64px;display:flex;align-items:center;justify-content:center;gap:14px}
.footer-brand .brand{color:var(--white);font-size:28px}
.footer-brand .brand-mark{width:44px;height:44px}
.back-top{left:971px;top:4771px;color:var(--white);font-size:14px;font-weight:700}
.top-square{left:1070px;top:4758px;width:43px;height:43px;background:var(--yellow);border-radius:3px;display:flex;align-items:center;justify-content:center}
.foot-rule{left:87px;top:4836px;width:1026px;height:1px;background:#2b3655}
.assess{top:4900px;color:var(--white);font-family:"Ubuntu",sans-serif;font-weight:500;font-size:26px}
.assess-copy{top:4948px;color:#d7dbe6;font-size:15px;line-height:26px}
.reach{position:absolute;top:5040px;display:flex;gap:16px;align-items:center;color:var(--white)}
.reach small{display:block;color:#b9c0d0;font-size:14px}
.reach b{font-size:15px}
.bottom-bar{left:0;top:5161px;width:1200px;height:59px;background:var(--navy-bar);color:#d7dbe6;font-size:13px}
</style>
</head>
<body>

<!-- Header -->
<header class="site-header">
  <div class="top-contact" style="left:126px">
    <span class="dot"><svg width="14" height="14" viewBox="0 0 24 24"><path fill="#fff" d="M6.6 10.8a15 15 0 006.6 6.6l2.2-2.2c.3-.3.7-.4 1-.2 1.1.4 2.3.6 3.6.6.6 0 1 .4 1 1V20c0 .6-.4 1-1 1A17 17 0 013 4c0-.6.4-1 1-1h3.5c.6 0 1 .4 1 1 0 1.3.2 2.5.6 3.6.1.3 0 .7-.2 1z"/></svg></span>
    <div><b>Call Us:</b>(208)555-0142</div>
  </div>
  <div class="top-contact" style="left:282px">
    <span class="dot"><svg width="14" height="14" viewBox="0 0 24 24"><path fill="#fff" d="M3 5h18v14H3z"/><path fill="none" stroke="#17315f" stroke-width="2" d="M3 6l9 7 9-7"/></svg></span>
    <div><b>Email:</b>office@riglineacademy.au</div>
  </div>
  <div class="btn appointment">BOOK APPOINTMENT</div>
  <div class="header-rule"></div>
  <nav class="nav">
    <a style="left:126px">Home</a>
    <a style="left:237px">About Us</a>
    <a style="left:389px">Services</a>
    <a style="left:707px">Gallery</a>
    <a style="left:845px">Our Team</a>
    <a style="left:969px">Contact Us</a>
  </nav>
</header>
<div class="logo-tab" style="z-index:4">
  <span class="brand-mark"></span>
  <span class="brand">Southern<br>Rigline Academy</span>
</div>

<!-- Hero -->
<section>
  <div class="photo hero-photo" role="img" aria-label="Excavator working in an open-cut quarry with rock walls"></div>
  <div class="abs hero-kicker">Experience</div>
  <h1 class="abs hero-title">Operator Training</h1>
  <div class="abs hero-line"></div>
  <p class="abs hero-copy">Lorem ipsum dolor sit amet, consectetur adipiscing elit, sed do eiusmod tempor ididunt ut labore et dolore magna aliqua</p>
  <div class="btn learn">LEARN MORE</div>
  <div class="btn quote">REQUEST QUOTE</div>
</section>

<!-- Features -->
<section>
  <div class="feature" style="left:93px">
    <div class="icon"><svg width="40" height="40" viewBox="0 0 40 40" fill="none" stroke="#ffc20e" stroke-width="2"><circle cx="20" cy="20" r="6"/><path d="M20 6v5M20 29v5M6 20h5M29 20h5M10 10l3.5 3.5M26.5 26.5L30 30M10 30l3.5-3.5M26.5 13.5L30 10"/></svg></div>
    <h3>Expertise</h3>
    <p>Lorem ipsum dolor sit amet, consect adipiscing elit, sed do eiusmod tempor incididunt ut labore et dolore</p>
  </div>
  <div class="feature" style="left:442px">
    <div class="icon"><svg width="40" height="40" viewBox="0 0 40 40" fill="none" stroke="#ffc20e" stroke-width="2"><circle cx="17" cy="18" r="11"/><path d="M6 18h22M17 7c4 4 4 18 0 22M17 7c-4 4-4 18 0 22"/><circle cx="28" cy="27" r="5"/></svg></div>
    <h3>Professional</h3>
    <p>Lorem ipsum dolor sit amet, consect adipiscing elit, sed do eiusmod tempor incididunt ut labore et dolore</p>
  </div>
  <div class="feature" style="left:788px">
    <div class="icon"><svg width="40" height="40" viewBox="0 0 40 40" fill="none" stroke="#ffc20e" stroke-width="2"><circle cx="20" cy="14" r="7"/><path d="M7 34c0-7 6-11 13-11s13 4 13 11z"/></svg></div>
    <h3>Experienced</h3>
    <p>Lorem ipsum dolor sit amet, consect adipiscing elit, sed do eiusmod tempor incididunt ut labore et dolore</p>
  </div>
</section>

<!-- About -->
<section>
  <div class="abs eyebrow" style="left:96px;top:1181px">See the difference &nbsp;—</div>
  <h2 class="abs heading about-title">Redefining the art of<br>Operator Training</h2>
  <p class="abs about-copy">Lorem ipsum dolor sit amet, consectetur adipiscing elit, sed do eius mod tempor incididunt ut labore et dolore magna aliqua. Ut enim ad minim veniam, quis nostrud exercitation ullamco laboris nisi ut aliquip ex ea commodo consequat. Duis aute irure dolor in Lorem ipsum dolor sit amet, consectetur adipiscing elit, sed do eius mod tempor incididunt ut labore et dolore magna aliqua. Ut enim ad minim veniam, quis nostrud exercitation ullamco laboris nisi ut aliquip ex ea commodo consequat. Duis aute irure dolor in</p>
  <div class="btn contact-btn">Contact us <svg width="16" height="12" viewBox="0 0 16 12" fill="none" stroke="#fff" stroke-width="1.8"><path d="M1 6h13M9 1l5 5-5 5"/></svg></div>
  <svg class="abs" style="left:530px;top:1293px" width="160" height="160" viewBox="0 0 160 160" fill="none" stroke="#7badd7" stroke-dasharray="3 4"><path d="M80 10A70 70 0 0 0 80 150"/><path d="M80 30A50 50 0 0 0 80 130"/></svg>
  <div class="photo about-photo" role="img" aria-label="Site worker in hard hat and hi-vis vest guiding a loader on a construction site"></div>
  <div class="abs badge"><span class="brand-mark" style="width:18px;height:18px;background:var(--navy)"></span></div>
</section>

<!-- Services -->
<section>
  <div class="abs services"></div>
  <div class="abs center eyebrow" style="top:1746px">— &nbsp;Our services&nbsp; —</div>
  <h2 class="abs center heading" style="top:1768px;font-size:34px">Services We Offer</h2>
  <p class="abs center section-copy" style="top:1833px">Lorem ipsum dolor sit amet, consectetur adipiscing elit, sed do eiusmod tempor incididunt ut<br>labore et dolore magna aliqua. Ut enim ad minim veniam, quis nostrud exercitation</p>
  <div class="service" style="left:91px;background:linear-gradient(135deg,#7fa7cf 0%,#d7b33a 55%,#5b5d4a 100%)" role="img" aria-label="Operator in hard hat standing beside a yellow excavator"></div>
  <div class="service" style="left:440px;background:linear-gradient(135deg,#d9c7a5 0%,#e27a2a 45%,#b8a47e 100%)" role="img" aria-label="Mine worker in hi-vis vest checking notes at a sand pit"></div>
  <div class="service" style="left:784px;background:linear-gradient(135deg,#c99a60 0%,#d7a54a 50%,#8a6a3f 100%)" role="img" aria-label="Excavator loading sand in a quarry"></div>
  <div class="service-label" style="left:126px">Civil Construction</div>
  <div class="service-label" style="left:478px">Mining</div>
  <div class="service-label" style="left:822px">Quarrying</div>
</section>

<!-- Call band -->
<section>
  <div class="photo call-band" role="img" aria-label="Dark close-up of heavy machinery"></div>
  <p class="abs center call-text">We're On <span>Call 24/7</span> to React Promptly to Your<br>Operator Training Needs</p>
  <div class="abs call-pill"><span>+ (08) 5550 2841</span><span>[or]</span><span>train@riglineacademy.au</span></div>
</section>

<!-- Projects -->
<section>
  <div class="abs projects-bg"></div>
  <div class="abs eyebrow" style="left:91px;top:2726px">See the difference &nbsp;—</div>
  <h2 class="abs heading" style="left:91px;top:2745px;font-size:34px">Our Recent Projects</h2>
  <div class="project" style="left:91px;background:linear-gradient(180deg,#6f9ed3 0%,#a8c3df 40%,#d2622a 70%,#b39a7a 100%)" role="img" aria-label="Orange excavator on a fenced work site"></div>
  <div class="project" style="left:409px;background:linear-gradient(180deg,#6a6f76 0%,#8f8a7a 40%,#c9c25a 70%,#3b3b3b 100%)" role="img" aria-label="Smiling site supervisor in hard hat with arms crossed"></div>
  <div class="project" style="left:726px;background:linear-gradient(180deg,#8db0d8 0%,#c7d4de 40%,#d8a52c 70%,#7a6a53 100%)" role="img" aria-label="Yellow wheel loader on a gravel yard"></div>
  <div class="project" style="left:1044px;background:linear-gradient(180deg,#8d98a3 0%,#a69a80 45%,#c9a43b 65%,#5d5446 100%)" role="img" aria-label="Excavator digging at a city development site"></div>
  <div class="project-label" style="left:91px">PROJECT 382 IN<br>SYDNEY</div>
  <div class="project-label" style="left:409px">PROJECT 382 IN<br>MELBOURNE</div>
  <div class="project-label" style="left:726px">PROJECT 382 IN<br>PERTH</div>
  <div class="project-label" style="left:1044px">PROJECT 382 IN<br>SYDNEY</div>
  <div class="btn projects-btn">Contact us <svg width="16" height="12" viewBox="0 0 16 12" fill="none" stroke="#fff" stroke-width="1.8"><path d="M1 6h13M9 1l5 5-5 5"/></svg></div>
</section>

<!-- Why choose us -->
<section>
  <div class="photo why-photo" role="img" aria-label="Operator in the cab of a yellow machine at sunset"></div>
  <div class="abs why-card">
    <div class="abs eyebrow" style="left:50px;top:60px">See the difference &nbsp;—</div>
    <h2 class="abs heading" style="left:50px;top:80px;font-size:34px">Why Choose Us?</h2>
    <div class="why-item" style="top:150px">
      <div class="ic"><svg width="36" height="36" viewBox="0 0 36 36" fill="none" stroke="#ffc20e" stroke-width="1.8"><path d="M6 22a12 12 0 0124 0"/><path d="M4 22h28M18 10v4M12 22v6M24 22v6"/></svg></div>
      <div><h4>Quality Assurance</h4><p>Lorem ipsum dolor sit amet, consectetur adipiscing elit, sed do eiusmod tempor incididunt ut labore et</p></div>
    </div>
    <div class="why-item" style="top:242px">
      <div class="ic"><svg width="36" height="36" viewBox="0 0 36 36" fill="none" stroke="#ffc20e" stroke-width="1.8"><path d="M18 4l4 9 10 1-7.5 6.5L27 31l-9-5-9 5 2.5-10.5L4 14l10-1z"/></svg></div>
      <div><h4>Proven Record</h4><p>Lorem ipsum dolor sit amet, consectetur adipiscing elit, sed do eiusmod tempor incididunt ut labore et</p></div>
    </div>
    <div class="why-item" style="top:334px">
      <div class="ic"><svg width="36" height="36" viewBox="0 0 36 36" fill="none" stroke="#ffc20e" stroke-width="1.8"><circle cx="16" cy="9" r="5"/><path d="M8 30l4-12h8l3 6h8M6 32h26"/></svg></div>
      <div><h4>Comprehensive Services</h4><p>Lorem ipsum dolor sit amet, consectetur adipiscing elit, sed do eiusmod tempor incididunt ut labore et</p></div>
    </div>
  </div>
</section>

<!-- Contact -->
<section>
  <div class="abs center eyebrow" style="top:3951px">— &nbsp;Contact us&nbsp; —</div>
  <h2 class="abs center heading" style="top:3972px;font-size:34px">Get In Touch With Us</h2>
  <p class="abs center section-copy" style="top:4034px">Lorem ipsum dolor sit amet, consectetur adipiscing elit, sed do eiusmod tempor incididunt ut<br>labore et dolore magna aliqua. Ut enim ad minim veniam, quis nostrud exercitation</p>
  <div class="abs form-card"></div>
  <div class="field active" style="left:195px;top:4180px;width:391px;height:39px"><label>Your Name</label>John</div>
  <div class="field" style="left:606px;top:4180px;width:391px;height:39px"><label>Your Website</label>www.riglineacademy.au</div>
  <div class="field" style="left:195px;top:4255px;width:391px;height:39px"><label>Your Phone</label>123 456 789</div>
  <div class="field" style="left:606px;top:4255px;width:391px;height:39px"><label>Your Email</label>hello@riglineacademy.au</div>
  <div class="field" style="left:195px;top:4330px;width:802px;height:148px;border-radius:14px"><label>Your Message</label>Type Message</div>
  <span class="social" style="left:209px" aria-label="Social profile"></span>
  <span class="social" style="left:246px" aria-label="Social profile"></span>
  <span class="social" style="left:285px" aria-label="Social profile"></span>
  <span class="social" style="left:323px" aria-label="Social profile"></span>
  <div class="btn submit">Submit Now <i></i></div>
</section>

<!-- Footer -->
<footer>
  <div class="abs footer"></div>
  <span class="foot-social" style="left:87px" aria-label="Social profile"></span>
  <span class="foot-social" style="left:137px" aria-label="Social profile"></span>
  <span class="foot-social" style="left:187px" aria-label="Social profile"></span>
  <span class="foot-social" style="left:236px" aria-label="Social profile"></span>
  <div class="abs footer-brand"><span class="brand-mark"></span><span class="brand">Southern<br>Rigline Academy</span></div>
  <div class="abs back-top">Back to top</div>
  <div class="abs top-square"><svg width="14" height="10" viewBox="0 0 14 10"><path fill="#fff" d="M7 1l6 8H1z"/></svg></div>
  <div class="abs foot-rule"></div>
  <h2 class="abs center assess">Get free assessment today</h2>
  <p class="abs center assess-copy">Lorem ipsum dolor sit amet, consectetur adipiscing elit, sed do eiusmod tempor<br>incididunt ut labore et dolore magna aliqua.</p>
  <div class="reach" style="left:219px">
    <svg width="50" height="50" viewBox="0 0 24 24" fill="none" stroke="#ffc20e" stroke-width="1.2"><path d="M6.6 10.8a15 15 0 006.6 6.6l2.2-2.2c.3-.3.7-.4 1-.2 1.1.4 2.3.6 3.6.6.6 0 1 .4 1 1V20c0 .6-.4 1-1 1A17 17 0 013 4c0-.6.4-1 1-1h3.5c.6 0 1 .4 1 1 0 1.3.2 2.5.6 3.6.1.3 0 .7-.2 1z"/></svg>
    <div><small>Make a Call</small><b>+61 8 5550 3010</b></div>
  </div>
  <div class="reach" style="left:478px">
    <svg width="50" height="50" viewBox="0 0 24 24" fill="none" stroke="#ffc20e" stroke-width="1.2"><path d="M3 9l9-6 9 6v11H3z"/><path d="M3 9l9 6 9-6M6 7h12v5"/></svg>
    <div><small>Mail Us On</small><b>hello@riglineacademy.au</b></div>
  </div>
  <div class="reach" style="left:758px">
    <svg width="50" height="50" viewBox="0 0 24 24" fill="none" stroke="#ffc20e" stroke-width="1.2"><path d="M12 21s-6-6-6-11a6 6 0 0112 0c0 5-6 11-6 11z"/><circle cx="12" cy="10" r="2.2"/><path d="M4 21h16"/></svg>
    <div><small>Location</small><b>48 Quarry Bend Rd</b></div>
  </div>
  <div class="abs bottom-bar">
    <span class="abs" style="left:85px;top:22px">Southern Rigline Academy</span>
    <span class="abs" style="left:801px;top:22px">Privacy Policy</span>
    <span class="abs" style="left:914px;top:22px">Terms &amp; Conditions</span>
    <span class="abs" style="left:1056px;top:22px">Site Map</span>
  </div>
</footer>

</body>
</html>
```